Professional violinist needs business cards

I am trying to attract the following jobs:
-private violin lessons (primarily classical)
-performance gigs (weddings, birthday parties, funerals, etc.)
-collaborations with other artists (studio recordings, performances)

I want to communicate that I have a very high standard of excellence for my work, but I also love people and celebrations.
Values/style words I like are:
love, joy, peace, fun, beauty, authenticity, excellence, warmth, refined/sleek, free spirited. If that's too confusing, just ignore :)

I will attach my favorite business card template that I could find on Canva. The lines are supposed to be like a music staff, which I think is really cool, but I also don't want it to look too busy. I like the simple black and white--I think it looks sharp--but I also am open to other ideas. I also have seen business cards with pictures included that looked great, so I attached an image that could be used as well.

I am also attaching a file that I made of my initials that could be used as a logo, but I'm not sure if it should be included.

Information on the card:
-My name (18 letters total)
-"violinist"
-phone number, email, website

Thank you!

```html
<!DOCTYPE html>
<html lang="en">
<head>
<meta charset="utf-8">
<title>Violinist Business Card</title>
<link href="https://fonts.googleapis.com/css2?family=Ubuntu:wght@300;500&display=swap" rel="stylesheet">
<style>
  :root {
    --page: #eeeeee;
    --navy: #1f2338;
    --paper: #fafafa;
    --staff: #e6e7ec;
    --ink: #1f2338;
  }
  * { margin: 0; padding: 0; box-sizing: border-box; }
  html, body { width: 1200px; height: 1200px; overflow: hidden; }
  body {
    background: var(--page);
    font-family: "Ubuntu", sans-serif;
    position: relative;
  }
  .card {
    position: absolute;
    left: 290px;
    width: 630px;
    height: 360px;
    border-radius: 26px;
    overflow: hidden;
  }
  .card-front { top: 185px; background: var(--navy); color: #fff; }
  .card-back { top: 635px; background: var(--paper); color: var(--ink); border: 1px solid #e2e2e2; }

  .identity { position: absolute; left: 45px; top: 46px; line-height: 30px; }
  .identity .name { font-weight: 500; font-size: 24px; }
  .identity .role { font-weight: 300; font-size: 24px; }

  .staff { position: absolute; left: 0; top: 0; width: 630px; height: 360px; }
  .staff line { stroke: var(--staff); stroke-width: 1.4; }

  .monogram {
    position: absolute;
    left: 366px;
    top: 100px;
    width: 215px;
    height: 205px;
    display: flex;
    align-items: center;
    justify-content: center;
    font-weight: 500;
    font-size: 128px;
    color: #fff;
    letter-spacing: -2px;
  }

  .contact {
    position: absolute;
    right: 30px;
    top: 54px;
    text-align: right;
    font-size: 21px;
    line-height: 27px;
  }
  .contact li { list-style: none; display: flex; justify-content: flex-end; align-items: center; gap: 12px; }
  .contact .phone { font-weight: 500; font-size: 22px; }
  .contact .email, .contact .web { font-weight: 300; }
  .contact svg { width: 22px; height: 22px; flex: none; }
  .contact svg * { fill: none; stroke: var(--ink); stroke-width: 1.6; }

  .services { position: absolute; left: 43px; top: 156px; list-style: none; }
  .services li { margin-bottom: 9px; line-height: 24px; }
  .services .service { display: block; font-weight: 500; font-size: 19.5px; }
  .services .detail { display: block; font-weight: 300; font-size: 20.5px; }
</style>
</head>
<body>
  <section class="card card-front">
    <div class="identity">
      <div class="name">Yournameis Hereyour</div>
      <div class="role">Violinist</div>
    </div>
    <svg class="staff" viewBox="0 0 630 360" aria-hidden="true">
      <line x1="0" y1="155" x2="366" y2="155"/><line x1="581" y1="155" x2="630" y2="155"/>
      <line x1="0" y1="192" x2="366" y2="192"/><line x1="581" y1="192" x2="630" y2="192"/>
      <line x1="0" y1="229" x2="366" y2="229"/><line x1="581" y1="229" x2="630" y2="229"/>
      <line x1="0" y1="266" x2="366" y2="266"/><line x1="581" y1="266" x2="630" y2="266"/>
      <line x1="0" y1="303" x2="366" y2="303"/><line x1="581" y1="303" x2="630" y2="303"/>
    </svg>
    <div class="monogram">YH</div>
  </section>

  <section class="card card-back">
    <ul class="contact">
      <li class="phone">8264 315 0972
        <svg viewBox="0 0 22 22" aria-hidden="true"><rect x="7" y="4" width="8" height="14" rx="1.5"/><line x1="10" y1="15.5" x2="12" y2="15.5"/></svg>
      </li>
      <li class="email">youremailishere@mailhub.com
        <svg viewBox="0 0 22 22" aria-hidden="true"><rect x="2" y="5" width="18" height="13" rx="1.5"/><polyline points="2.5,6 11,13 19.5,6"/></svg>
      </li>
      <li class="web">yourviolinstudiosite.com
        <svg viewBox="0 0 22 22" aria-hidden="true"><circle cx="11" cy="11" r="8"/><ellipse cx="11" cy="11" rx="3.5" ry="8"/><line x1="3" y1="11" x2="19" y2="11"/><line x1="4.5" y1="7" x2="17.5" y2="7"/><line x1="4.5" y1="15" x2="17.5" y2="15"/></svg>
      </li>
    </ul>
    <ul class="services">
      <li><span class="service">Private violin lessons</span><span class="detail">(primarily classical)</span></li>
      <li><span class="service">Performance gigs</span><span class="detail">(weddings, birthday parties, funerals, etc.)</span></li>
      <li><span class="service">Collaborations with other artists</span><span class="detail">(studio recordings, performances)</span></li>
    </ul>
  </section>
</body>
</html>
```